Electrical Contractor needs new Flyer

Update: need this flyer asap due to the flyer drop deadline coming soon.
Job Intro:
Design a DL Colour Flyer for a small Electrical Contracting company in the Eastern Suburbs of Melbourne VIC.
Specs:
Size: 99mmx210mm DL.
Paper to be printed on: 150gsm Glossy Paper.
PSD/PDF file must include bleed/crop marks.
Type: Double Sided
Colour: Front and Rear to be FULL colour.
Note: Thanks for the black and white flyers so far, but i think due to the fact iam paying for colour printing anyway, i will go only with colour. (unless you can show me otherwise that black and white can stand out better than colour)
Aim: To Target Local Customers in the area with a flyer that grabs there attention and makes them want to read more, instead of throwing out the flyer.
(there is allready other people putting out flyers in area)
Front Page Includes:
Company name: Calder Brook Electrical
REC: 48736 (can be small txt in a corner on front side, is legaly required to be displayed)
Phone: 1300 574 628
website: www.cbsparkworks.com.au
not required but happy to include:
Facebook Logo
www.facebook.com/cbsparkworks
include visa/mastercard pics
Rear of flyer:
to include work we do etc
We do not have a logo yet for our company, please feel free to design something to suite (keep in mind copyright etc)
you may read our website for info on what we do, but please dont use pictures of jobs etc from our work page. and try not just copy paste text into the flyer. (i can do that myself thats why im getting a designer to add the wow factor to it.
Looking for a Fresh modern looking flyer that will really get the readers attention.
(please no cheap looking cartons pics, also would like australian based looking cables, products if you are using pictures)
any more info please ask me thanks
I have included pics for ref, (such as my current cards and ute signage) please use as examples but dont just base the design on those thanks.
Also inc was my old flyers, i made them ,but they dont fit into the new DL flyer size so need to be re-sized etc.
Note: we may edit or change the winning design in future and this flyer will be copyright to us.

```html
<!DOCTYPE html>
<html lang="en">
<head>
<meta charset="utf-8">
<title>Calder Brook Electrical – DL Flyer Rear</title>
<link href="https://fonts.googleapis.com/css2?family=Arimo:wght@400;700&family=Roboto+Condensed:wght@300;400;700&display=swap" rel="stylesheet">
<style>
  :root {
    --backdrop: #233230;
    --ink-black: #000000;
    --paper-white: #ffffff;
    --text-dark: #111111;
    --text-muted: #8c8c8c;
    --accent-electric: #f4b416;
    --accent-blue: #1f7fc4;
    --seal-blue: #4a86c2;
    --seal-rim: #c9d3dd;
  }
  * { box-sizing: border-box; margin: 0; padding: 0; }
  html, body {
    width: 991px;
    height: 1200px;
    overflow: hidden;
    background: var(--backdrop);
  }
  .flyer {
    position: absolute;
    left: 334px;
    top: 117px;
    width: 433px;
    height: 914px;
    background: var(--ink-black);
    font-family: "Arimo", Arial, sans-serif;
  }

  .intro {
    height: 281px;
    padding: 20px 18px 0 36px;
    color: var(--paper-white);
    font-size: 15px;
    line-height: 18.5px;
    border-bottom: 4px solid var(--accent-electric);
  }
  .licence {
    text-align: right;
    font-family: "Roboto Condensed", "Arial Narrow", sans-serif;
    font-weight: 700;
    font-size: 19px;
    line-height: 20px;
    margin-bottom: 14px;
  }
  .intro p { padding-right: 10px; }
  .intro p + p { margin-top: 18.5px; }
  .company-name { font-weight: 700; font-size: 17.5px; }

  .promise {
    position: relative;
    height: 396px;
    margin-top: -4px;
    border-top: 4px solid var(--accent-electric);
    background: var(--paper-white);
    color: var(--text-dark);
    padding: 8px 22px 0 36px;
  }
  .promise-title {
    font-weight: 700;
    font-size: 18px;
    line-height: 22px;
    color: var(--accent-blue);
    margin-bottom: 20px;
  }
  .promise-list { list-style: none; }
  .promise-list li {
    position: relative;
    font-size: 15px;
    line-height: 18.5px;
    margin-bottom: 18.5px;
  }
  .promise-list li::before {
    content: "";
    position: absolute;
    left: -19px;
    top: 4px;
    width: 11px;
    height: 11px;
    border-radius: 50%;
    background: var(--accent-blue);
  }
  .guarantee-seal {
    position: absolute;
    left: 331px;
    top: 319px;
    width: 66px;
    height: 66px;
  }

  .contact {
    height: 237px;
    padding-top: 17px;
    text-align: center;
    color: var(--paper-white);
    font-family: "Roboto Condensed", "Arial Narrow", sans-serif;
  }
  .service-areas {
    font-weight: 300;
    font-size: 21px;
    line-height: 28px;
  }
  .emergency {
    margin-top: 12px;
    font-weight: 300;
    font-size: 17px;
    line-height: 22px;
    color: var(--text-muted);
  }
  .phone {
    margin-top: 10px;
    font-family: "Arimo", Arial, sans-serif;
    font-weight: 700;
    font-size: 29px;
    line-height: 34px;
    color: var(--accent-electric);
  }
  .website {
    margin-top: 6px;
    font-weight: 300;
    font-size: 26px;
    line-height: 32px;
  }
</style>
</head>
<body>
  <main class="flyer">
    <section class="intro">
      <div class="licence">REC: 48736</div>
      <p><span class="company-name">Calder Brook Electrical</span> Contractors is a privately Family owned and operated company providing a comprehensive range of domestic and commercial electrical services throughout Victoria.</p>
      <p>We provide a broad range of electrical services including small electrical jobs around the home to larger commercial electrical works. Our business is underpinned by a commitment to customer service, that is, we turn up on time, we provide quality workmanship at a fair and competitive price.</p>
    </section>

    <section class="promise">
      <h2 class="promise-title">Our Promise to you:</h2>
      <ul class="promise-list">
        <li>We arrive on time. (And keep you up to date, with SMS/Email/PH Job Tracking)</li>
        <li>You will always know the cost before we start the job.</li>
        <li>We Clean up after our selves, leaving your home like it was before we arrived.</li>
        <li>We give you 12months Warranty on all parts, or longer if product has own warranty.</li>
        <li>If theres any problem and its our fault, we will fix it at no cost to you.</li>
        <li>We offer Friendly, helpful Service and Advise.</li>
        <li>We dont charge any Call out Fees</li>
      </ul>
      <svg class="guarantee-seal" viewBox="0 0 66 66" role="img" aria-label="Satisfaction guarantee seal">
        <circle cx="33" cy="33" r="30" fill="var(--seal-blue)" stroke="var(--seal-rim)" stroke-width="4"/>
      </svg>
    </section>

    <section class="contact">
      <p class="service-areas">Electrician, Electrical Contractor, Electrics,<br>Lilydale, Ringwood, Croydon, Mooroolbark,<br>Healesville, mt evelyn, chirnside park</p>
      <p class="emergency">24 hour 7 day emergency service</p>
      <p class="phone">1300 574 628</p>
      <p class="website">WWW.CBSPARKWORKS.COM.AU</p>
    </section>
  </main>
</body>
</html>
```